New Optometry Practice needs a Business Card

Need a business card for an Optometry practice called 'Marlow Vista Eyecare'. I would like to use designs that are friendly, fun and professional. Looking to incorporate glasses (see uploaded image). Not interested in design with an 'eye' in logo. Like green, blue, white as color choices..but open to your ideas. Back of card will be an appointment card as well as provide address, phone and email information.

Industry/Entity Type

Business

Contact Information for Business Card

Marlow Vista Eyecare
Dr. Petra Lindqvist, Optometrist (or O.D.)
4172 S Corbell Ave Wenatchee, WA 98736
PMarlowvistaeyecare.example

Colors
acd036
33b8a4
f68d4e
cfeae6
fee18a
cadf82

Requirements
Must have
• Appointment card on back with date/time of return for next exam

```html
<!DOCTYPE html>
<html lang="en">
<head>
<meta charset="utf-8">
<title>Marlow Vista Eyecare – Business Card</title>
<link href="https://fonts.googleapis.com/css2?family=Open+Sans:wght@400;600&display=swap" rel="stylesheet">
<style>
  :root {
    --stage: #000000;
    --card-front: #f3f3f3;
    --card-back: #ffffff;
    --brand-blue: #3ba1de;
    --ink: #111111;
    --dots: #111111;
  }
  * { margin: 0; padding: 0; box-sizing: border-box; }
  html, body { width: 1200px; height: 900px; overflow: hidden; background: var(--stage); }
  body { position: relative; font-family: "Open Sans", Arial, sans-serif; color: var(--ink); }

  .card { position: absolute; top: 200px; width: 310px; height: 502px; }
  .card--front { left: 265px; background: var(--card-front); border-radius: 62px 0 62px 0; }
  .card--back { left: 641px; width: 309px; background: var(--card-back); border-radius: 0 62px 0 62px; }

  .wordmark {
    position: absolute; right: 30px; text-align: right;
    color: var(--brand-blue); font-weight: 400; text-transform: uppercase; line-height: 1.1;
  }
  .card--front .wordmark { top: 132px; font-size: 37px; letter-spacing: -0.5px; }
  .card--back .wordmark { top: 49px; font-size: 37px; letter-spacing: -0.5px; }
  .wordmark__line2 { display: block; font-size: 25px; letter-spacing: 1.5px; }

  .brand-square {
    position: absolute; left: 125px; top: 58px; width: 54px; height: 54px; background: var(--brand-blue);
  }

  .person { position: absolute; left: 31px; top: 299px; }
  .person__name { color: var(--brand-blue); font-weight: 600; font-size: 17.5px; }
  .person__role { font-size: 13px; margin-top: 1px; }

  .address { position: absolute; left: 31px; top: 358px; font-size: 13.5px; line-height: 21px; font-style: normal; }

  .contact { position: absolute; left: 31px; top: 413px; list-style: none; font-size: 13.5px; }
  .contact li { display: flex; align-items: center; height: 21px; }
  .contact svg { width: 11px; height: 11px; margin-right: 9px; fill: var(--brand-blue); flex-shrink: 0; }

  .appointment { position: absolute; left: 16px; right: 18px; top: 338px; color: var(--brand-blue); font-weight: 600; font-size: 14.5px; }
  .appointment__title { text-align: center; font-size: 16.5px; margin-bottom: 18px; }
  .appointment__row { display: flex; align-items: baseline; margin-bottom: 22px; white-space: nowrap; }
  .appointment__fill { flex: 1; border-bottom: 2px dotted var(--dots); margin: 0 4px 0 5px; height: 1px; position: relative; top: -3px; }
  .appointment__fill--short { flex: 0 0 86px; margin-right: 5px; }
</style>
</head>
<body>
  <section class="card card--front" aria-label="Card front">
    <div class="brand-square" aria-hidden="true"></div>
    <h1 class="wordmark">Marlow Vista<span class="wordmark__line2">Eyecare</span></h1>

    <div class="person">
      <p class="person__name">Dr. Petra Lindqvist</p>
      <p class="person__role">Optometrist</p>
    </div>

    <address class="address">4172 S Corbell Ave<br>Wenatchee, WA 98736</address>

    <ul class="contact">
      <li><svg viewBox="0 0 12 12" aria-hidden="true"><path d="M2.5 0.5 L4.3 2.6 3.4 4 Q4.6 6.9 8 8.6 L9.4 7.7 11.5 9.5 10.3 11.3 Q4.8 11 0.7 1.7 Z"/></svg>(055)-318-2046</li>
      <li><svg viewBox="0 0 12 12" aria-hidden="true"><path d="M0 2 H12 V10 H0 Z M0.8 2.6 L6 6.6 11.2 2.6" fill-rule="evenodd"/><path d="M0.5 2.4 L6 6.8 11.5 2.4" stroke="#f3f3f3" stroke-width="1" fill="none"/></svg>hello@marlowvista.example</li>
      <li><svg viewBox="0 0 12 12" aria-hidden="true"><circle cx="6" cy="6" r="5.5"/><path d="M0.5 6 H11.5 M6 0.5 Q2.8 6 6 11.5 M6 0.5 Q9.2 6 6 11.5" stroke="#f3f3f3" stroke-width="0.8" fill="none"/></svg>www.PMarlowvistaeyecare.example</li>
    </ul>
  </section>

  <section class="card card--back" aria-label="Card back">
    <h2 class="wordmark">Marlow Vista<span class="wordmark__line2">Eyecare</span></h2>

    <div class="appointment">
      <p class="appointment__title">Appointment</p>
      <p class="appointment__row">Name :<span class="appointment__fill"></span></p>
      <p class="appointment__row">Date :<span class="appointment__fill appointment__fill--short"></span>Time :<span class="appointment__fill"></span></p>
    </div>
  </section>
</body>
</html>
```